Business Card Design Project for Architecture and Interior Design company

We need a business card design and logo for an architecture and design firm located in Santiago de Chile. It´s a small company, and the name is "Vostiq" ("Vost" from my surname Vostani, and "arq" for arquitectura or architecture. But it would also be nice that the logo comunicates de Word game "Vosta" as beautiful in italian, and "arq" as architecture".
The idea is to give a delicate, elegant and sofisticated, yet fresh image. Would prefer grey black and white colors, but wouldn´t mind to use another additional color.
I allready have a web page www.vostiq.cl, but would like to improve the logo design.
Please contact if any further information is requiered.
Reason: Need a more arquitectural and desing spirit in the cards. Few of them give that idea.

```html
<!DOCTYPE html>
<html lang="es">
<head>
<meta charset="utf-8">
<title>Vostiq – Tarjeta de presentación</title>
<link href="https://fonts.googleapis.com/css2?family=Questrial&family=Open+Sans:wght@400;700&display=swap" rel="stylesheet">
<style>
  :root {
    --page-bg: #c4c4c2;
    --card-white: #ffffff;
    --ink-grey: #4a4a4a;
    --panel-dark: #484848;
    --rule-grey: #8c8c8c;
    --text-light: #ffffff;
    --accent-red: #d9261c;
    --accent-orange: #f0880a;
    --accent-yellow: #f1e11c;
  }
  * { margin: 0; padding: 0; box-sizing: border-box; }
  html, body {
    width: 1200px;
    height: 848px;
    overflow: hidden;
    background: var(--page-bg);
  }
  .canvas {
    position: relative;
    width: 1200px;
    height: 848px;
  }
  .card {
    position: absolute;
    top: 281px;
    width: 467px;
    height: 285px;
    background: var(--card-white);
  }
  .card--front { left: 91px; }
  .card--back { left: 641px; }

  .wordmark {
    position: absolute;
    left: 0;
    top: 0;
    width: 100%;
    height: 100%;
    display: flex;
    align-items: center;
    justify-content: center;
    font-family: "Questrial", sans-serif;
    font-size: 64px;
    color: var(--ink-grey);
    letter-spacing: 1px;
  }

  .info-panel {
    position: absolute;
    left: 26px;
    top: 27px;
    width: 413px;
    height: 231px;
    background: var(--panel-dark);
    color: var(--text-light);
    font-family: "Open Sans", sans-serif;
  }
  .holder {
    position: absolute;
    left: 18px;
    top: 26px;
    font-size: 13px;
    font-weight: 700;
    line-height: 19px;
  }
  .holder-rule {
    position: absolute;
    left: 18px;
    top: 73px;
    width: 372px;
    height: 2px;
    background: var(--rule-grey);
  }
  .contact-list {
    position: absolute;
    left: 21px;
    top: 89px;
    list-style: none;
    font-size: 13px;
    line-height: 21px;
  }
  .contact-list li {
    display: flex;
    align-items: center;
  }
  .swatch {
    width: 15px;
    height: 15px;
    margin-right: 9px;
    flex: none;
  }
  .swatch--red { background: var(--accent-red); }
  .swatch--orange { background: var(--accent-orange); }
  .swatch--yellow { background: var(--accent-yellow); }
  .panel-mark {
    position: absolute;
    right: 18px;
    bottom: 14px;
    font-family: "Questrial", sans-serif;
    font-size: 18px;
    color: var(--text-light);
  }
</style>
</head>
<body>
<main class="canvas">
  <section class="card card--front" aria-label="Anverso">
    <div class="wordmark">Vostiq.</div>
  </section>

  <section class="card card--back" aria-label="Reverso">
    <div class="info-panel">
      <p class="holder">Mira Vostani Kelwal<br>Arquitecto</p>
      <div class="holder-rule"></div>
      <ul class="contact-list">
        <li><span class="swatch swatch--red"></span>+569 40512278</li>
        <li><span class="swatch swatch--orange"></span>mvostani@vostiq.cl</li>
        <li><span class="swatch swatch--yellow"></span>www.vostiq.cl</li>
      </ul>
      <div class="panel-mark">Vostiq</div>
    </div>
  </section>
</main>
</body>
</html>
```